Wordpress Design for crazy innovation company

I need an wordpress design for a hosted wordpress site. I have a new logo for the company, but no corporate design guide/color palette etc.

The main features of the website is a blog and a reference section.

Reference section structure:
About us
How to (with subpages)
Entrepreneurship (with subpages)
Links

Blog items
I will use keywords and comments, categories and tags.
Images will be used and should be clickable to see larger picture.

See qorvellabs.example for some sample content (in norwegian).

Nature of business:
- Qorvel Labs is a small innovative company guiding entrepreneurs and invests in tech startups (business angel) software and electronics. And in addition have a few crazy projects building prototypes for new electronics, software and apps.
- my background: software, hardware, marketing, sales

Inspiration websites:
http://foundersketchbookhall.example
http://wirelumen.example
http://plumgallery.example/item/grumpy/full_screen_preview/31746
http://www.tarnicstudio.example/themes/preview/?item=delta
http://moxbristle.example
http://www.lanternwharfworks.example

Favourite colors:
- pink
- orange
Updates

Instead of creating a bunch of custom css/html, i would like the final design to be based on the http://www.brindlekits.example/2012/06/easel/ theme.

Target Market(s)

entrepreneurs & investors

Industry/Entity Type

Software

Requirements
Must have
• Deliverables:
- Photoshop PSD/Illustrator AI files
- CSS/HTML suited for wordpress hosted

```html
<!DOCTYPE html>
<html lang="en">
<head>
<meta charset="utf-8">
<title>Qorvel Labs</title>
<link href="https://fonts.googleapis.com/css2?family=Yanone+Kaffeesatz:wght@400;700&family=Arvo:wght@400;700&family=Noto+Serif:wght@400;700&family=Open+Sans:wght@400&display=swap" rel="stylesheet">
<style>
:root{
  --pink:#ef0e6b;
  --blue:#38a6e0;
  --sky:#7fd0f5;
  --ink:#1c1c1c;
  --bar:#1f1f1f;
  --paper:#efefed;
  --rule:#d6d6d3;
  --frame:#e4e4de;
  --text:#9a9a9a;
  --side:#2e2e2e;
  --side-head:#0e0e0e;
  --side-text:#a5a5a5;
}
*{box-sizing:border-box;margin:0;padding:0}
html,body{width:1200px;height:2276px;overflow:hidden}
body{background:var(--paper);font-family:"Noto Serif",Georgia,serif;color:var(--ink);position:relative}
a{color:inherit}

.top-bar{position:absolute;left:0;top:0;width:1200px;height:58px;background:var(--bar)}
.top-bar__edge{position:absolute;left:0;top:58px;display:block}
.top-nav{position:absolute;left:71px;top:12px;display:flex;gap:51px;font-family:"Yanone Kaffeesatz",sans-serif;font-weight:700;font-size:25px;color:var(--pink);letter-spacing:.5px}
.search{position:absolute;left:830px;top:14px;width:294px;height:30px;border-radius:15px;background:#f5f5f5}
.search svg{position:absolute;right:10px;top:7px}

.brand{position:absolute;left:361px;top:99px;display:flex;align-items:center;gap:22px}
.brand__mark{width:97px;height:100px;background:var(--blue)}
.brand__name{font-family:"Yanone Kaffeesatz",sans-serif;font-size:84px;font-weight:400;color:var(--ink);letter-spacing:1px;line-height:1}

.rule{position:absolute;left:61px;width:1074px;height:2px;background:var(--rule)}

.section-tile{position:absolute;top:265px;width:321px}
.section-tile__title{font-family:"Yanone Kaffeesatz",sans-serif;font-size:50px;text-align:center;height:60px;line-height:50px;letter-spacing:.5px}
.section-tile__box{position:relative;height:256px;color:#fff}
.section-tile__box--blue{background:var(--blue)}
.section-tile__box--pink{background:var(--pink)}
.section-tile__lead{position:absolute;right:10px;top:50px;text-align:right;font-family:"Arvo",serif;font-weight:700;line-height:1}
.section-tile__lead span{display:block}
.l1{font-size:33px}
.l2{font-size:52px;color:var(--ink);margin:2px 0}
.l3{font-size:33px}
.section-tile__text{position:absolute;left:16px;top:188px;font-family:"Open Sans",sans-serif;font-size:15px;line-height:20px}
.section-tile__more{position:absolute;right:0;bottom:0;width:53px;height:53px;display:flex;align-items:center;justify-content:center}
.more--pink{background:var(--pink)}
.more--dark{background:var(--ink)}
.more--sky{background:var(--sky)}
.emblem{position:absolute;left:16px;top:58px;width:70px;height:70px;border:3px solid #fff}

.post{position:absolute;left:74px;width:685px;height:682px;background:#fff;border:9px solid var(--frame)}
.post__date{position:absolute;left:-46px;top:-36px;width:82px;height:82px;border-radius:50%;background:var(--pink);border:5px solid #fff;box-shadow:0 0 0 2px #e2e2e2;color:#fff;text-align:center;font-family:"Arvo",serif}
.post__day{display:block;font-size:30px;font-weight:700;margin-top:9px;line-height:1}
.post__month{display:block;font-size:11px;font-weight:700;letter-spacing:1px}
.post__title{position:absolute;left:47px;top:32px;font-family:"Arvo",serif;font-weight:400;font-size:42px;letter-spacing:.5px}
.post__line{position:absolute;left:46px;top:93px;width:570px;height:1px;background:#d9d9d9}
.post__media{position:absolute;left:46px;top:130px;width:570px;height:246px;background:radial-gradient(ellipse at 45% 50%,#4a3b2a,#241a14 55%,#0f0c0a)}
.post__zoom{position:absolute;left:246px;top:84px}
.post__body{position:absolute;left:46px;top:424px;width:572px;font-size:14px;line-height:19px;color:var(--text)}
.post__body p{margin-bottom:19px}
.post__keys{position:absolute;left:46px;top:616px;font-size:15px;font-weight:700;color:#333}
.post__keys a{color:var(--pink);font-weight:400;font-size:14px}
.post__keyline{position:absolute;left:46px;top:640px;width:518px;height:2px;background:#999}
.post__count{position:absolute;left:574px;top:603px;width:44px;height:38px;background:var(--blue);color:#fff;font-family:"Arvo",serif;font-size:14px;text-align:center;line-height:44px}
.post__count::before{content:"";position:absolute;left:0;top:-9px;border-left:12px solid var(--blue);border-top:9px solid transparent}

.sidebar{position:absolute;left:798px;top:683px;width:323px;background:var(--side)}
.widget__head{height:56px;background:var(--side-head);color:var(--pink);font-family:"Arvo",serif;font-size:29px;padding:8px 12px}
.widget__head--blue{color:var(--blue)}
.widget__head--white{color:#fff}
.widget__body{padding:14px 20px 0 20px;font-size:13px;color:var(--side-text)}
.icons{display:grid;grid-template-columns:repeat(7,33px);gap:12px 12.5px;padding:10px 0 0 8px}
.icons span{width:33px;height:33px;border-radius:5px}
.arrow-list{list-style:none}
.arrow-list li{position:relative;padding-left:16px;margin-bottom:15px;color:var(--blue);font-size:14px;line-height:17px}
.arrow-list li::before{content:"»";position:absolute;left:0;top:-1px;color:var(--pink)}
.arrow-list a{text-decoration:underline}
.dot-list{list-style:none}
.dot-list li{position:relative;padding:6px 0 6px 16px;border-bottom:1px dashed #555;line-height:17px}
.dot-list--plain li{border:none;padding:4px 0 4px 16px;color:#ddd}
.dot-list li::before{content:"";position:absolute;left:2px;top:13px;width:5px;height:5px;border-radius:50%;background:var(--pink)}
.newsletter__text{font-size:12px;line-height:16px;color:var(--side-text);margin:-4px -8px 12px}
.newsletter__form{position:relative;height:30px;border-radius:15px;background:#f2f2f2;margin:0 -8px}
.newsletter__form span{position:absolute;left:14px;top:8px;font-family:"Open Sans",sans-serif;font-size:10px;color:#999;letter-spacing:.5px}
.newsletter__form b{position:absolute;right:0;top:0;width:74px;height:30px;border-radius:15px;background:var(--pink);color:#fff;font-family:"Open Sans",sans-serif;font-size:12px;text-align:center;line-height:30px}
</style>
</head>
<body>

<header class="top-bar">
  <nav class="top-nav"><span>ABOUT US</span><span>HOW TO</span><span>ENTREPRENEURSHIP</span></nav>
  <div class="search">
    <svg width="16" height="16" viewBox="0 0 16 16"><circle cx="6.5" cy="6.5" r="4.5" fill="none" stroke="#38a6e0" stroke-width="2"/><line x1="10" y1="10" x2="14" y2="14" stroke="#38a6e0" stroke-width="2.5" stroke-linecap="round"/></svg>
  </div>
</header>
<svg class="top-bar__edge" width="1200" height="6">
  <defs><pattern id="zig" width="8" height="6" patternUnits="userSpaceOnUse"><polygon points="0,0 8,0 4,6" fill="#1f1f1f"/></pattern></defs>
  <rect width="1200" height="6" fill="url(#zig)"/>
</svg>

<div class="brand"><div class="brand__mark"></div><div class="brand__name">QORVEL LABS</div></div>

<div class="rule" style="top:237px"></div>

<section class="section-tile" style="left:76px">
  <h2 class="section-tile__title">ABOUT US</h2>
  <div class="section-tile__box section-tile__box--blue">
    <div class="emblem"></div>
    <div class="section-tile__lead"><span class="l1">Lorem</span><span class="l2">Ipsum</span><span class="l3">Dolor</span></div>
    <p class="section-tile__text">Lorem ipsum dolor sit amet.<br>This is just a dummy text.</p>
    <div class="section-tile__more more--pink"><svg width="20" height="20"><path d="M10 2v16M2 10h16" stroke="#fff" stroke-width="4"/></svg></div>
  </div>
</section>
<section class="section-tile" style="left:437px">
  <h2 class="section-tile__title">HOW TO</h2>
  <div class="section-tile__box section-tile__box--pink">
    <div class="section-tile__lead"><span class="l1">Lorem</span><span class="l2">Ipsum</span><span class="l3">Dolor</span></div>
    <p class="section-tile__text">Lorem ipsum dolor sit amet.<br>This is just a dummy text.</p>
    <div class="section-tile__more more--dark"><svg width="20" height="20"><path d="M10 2v16M2 10h16" stroke="#fff" stroke-width="4"/></svg></div>
  </div>
</section>
<section class="section-tile" style="left:800px">
  <h2 class="section-tile__title">ENTREPRENEURSHIP</h2>
  <div class="section-tile__box section-tile__box--blue">
    <div class="section-tile__lead"><span class="l1">Lorem</span><span class="l2">Ipsum</span><span class="l3">Dolor</span></div>
    <p class="section-tile__text">Lorem ipsum dolor sit amet.<br>This is just a dummy text.</p>
    <div class="section-tile__more more--sky"><svg width="20" height="20"><path d="M10 2v16M2 10h16" stroke="#1c1c1c" stroke-width="4"/></svg></div>
  </div>
</section>

<div class="rule" style="top:633px"></div>

<article class="post" style="top:680px">
  <div class="post__date"><span class="post__day">15</span><span class="post__month">SEPT</span></div>
  <h1 class="post__title">Smooth entry</h1>
  <div class="post__line"></div>
  <div class="post__media" role="img" aria-label="Dimmed photo of an audience behind a learn, build, code, data cycle diagram">
    <svg class="post__zoom" width="78" height="78" viewBox="0 0 78 78"><circle cx="39" cy="39" r="36" fill="#ef0e6b" stroke="#fff" stroke-width="4"/><circle cx="36" cy="36" r="8" fill="none" stroke="#fff" stroke-width="3"/><line x1="42" y1="42" x2="48" y2="48" stroke="#fff" stroke-width="4" stroke-linecap="round"/></svg>
  </div>
  <div class="post__body">
    <p>Agile establishment five principles:</p>
    <p>1. Entrepreneurship is everywhere. Not only in entrepreneurial companies, but also in etatablerte companies to launch new products and services.</p>
    <p>2. Entrepreneurship is management. Entrepreneurship is not just a new product and business development, but also management specifically geared towards extreme uncertainty.</p>
  </div>
  <div class="post__keys">Keywords: <a href="#">learn startup</a> , <a href="#">supple entry</a></div>
  <div class="post__keyline"></div>
  <div class="post__count">73</div>
</article>

<article class="post" style="top:1437px">
  <div class="post__date"><span class="post__day">15</span><span class="post__month">SEPT</span></div>
  <h1 class="post__title">Smooth entry</h1>
  <div class="post__line"></div>
  <div class="post__media" role="img" aria-label="Dimmed photo of an audience behind a learn, build, code, data cycle diagram">
    <svg class="post__zoom" width="78" height="78" viewBox="0 0 78 78"><circle cx="39" cy="39" r="36" fill="#ef0e6b" stroke="#fff" stroke-width="4"/><circle cx="36" cy="36" r="8" fill="none" stroke="#fff" stroke-width="3"/><line x1="42" y1="42" x2="48" y2="48" stroke="#fff" stroke-width="4" stroke-linecap="round"/></svg>
  </div>
  <div class="post__body">
    <p>Agile establishment five principles:</p>
    <p>1. Entrepreneurship is everywhere. Not only in entrepreneurial companies, but also in etatablerte companies to launch new products and services.</p>
    <p>2. Entrepreneurship is management. Entrepreneurship is not just a new product and business development, but also management specifically geared towards extreme uncertainty.</p>
  </div>
  <div class="post__keys">Keywords: <a href="#">learn startup</a> , <a href="#">supple entry</a></div>
  <div class="post__keyline"></div>
  <div class="post__count">73</div>
</article>

<aside class="sidebar">
  <section class="widget">
    <h3 class="widget__head">Social Profiles</h3>
    <div class="widget__body" style="height:218px;padding:0">
      <div class="icons">
        <span style="background:#e07b2a"></span><span style="background:#555"></span><span style="background:#4a6a8f"></span><span style="background:#c8513f"></span><span style="background:#3b5998"></span><span style="background:#4a4a7a"></span><span style="background:#5a8ec9"></span>
        <span style="background:#e8a21c"></span><span style="background:#5a7d3a"></span><span style="background:#c9322b"></span><span style="background:#2a75b0"></span><span style="background:#b7413e"></span><span style="background:#4f8fd1"></span><span style="background:#3a66b0"></span>
        <span style="background:#5aa832"></span><span style="background:#4c8a3c"></span><span style="background:#d77a2a"></span><span style="background:#8a8a8a"></span><span style="background:#3a9ad0"></span><span style="background:#5aa832"></span><span style="background:#3a5b7a"></span>
        <span style="background:#4aa0d5"></span><span style="background:#6a7fa0"></span><span style="background:#3ab0c8"></span><span style="background:#333"></span><span style="background:#d0a060"></span><span style="background:#555"></span><span style="background:#c4302b"></span>
      </div>
    </div>
  </section>
  <section class="widget">
    <h3 class="widget__head">Last Posts</h3>
    <div class="widget__body" style="height:196px;padding-top:18px">
      <ul class="arrow-list">
        <li><a href="#">Smooth entry</a></li>
        <li><a href="#">How larchmart funded startup?</a></li>
        <li><a href="#">What is the motivation for starting a business?</a></li>
        <li><a href="#">Welcome to the blog</a></li>
      </ul>
    </div>
  </section>
  <section class="widget">
    <h3 class="widget__head">Popular Posts</h3>
    <div class="widget__body" style="height:106px;padding-top:18px">
      <ul class="arrow-list">
        <li><a href="#">Smooth entry</a></li>
        <li><a href="#">How larchmart funded startup?</a></li>
      </ul>
    </div>
  </section>
  <section class="widget">
    <h3 class="widget__head">Categories</h3>
    <div class="widget__body" style="height:139px;padding-top:10px">
      <ul class="dot-list"><li>Category 1</li><li>Category 2</li><li>Category 3</li></ul>
    </div>
  </section>
  <section class="widget">
    <h3 class="widget__head">Key Words</h3>
    <div class="widget__body" style="height:127px;padding-top:10px">
      <ul class="dot-list"><li>Financing college in london coursenest learn</li><li>startup Passion sabbatical smooth entry</li></ul>
    </div>
  </section>
  <section class="widget">
    <h3 class="widget__head">Archive</h3>
    <div class="widget__body" style="height:138px;padding-top:12px">
      <ul class="dot-list dot-list--plain"><li>Spetember2012</li><li>August2012</li><li>July2012</li><li>June2012</li></ul>
    </div>
  </section>
  <section class="widget">
    <h3 class="widget__head widget__head--blue">Newsletter</h3>
    <div class="widget__body" style="height:117px">
      <p class="newsletter__text">Enter your email address to follow this blog and receive notifications of new posts by email.</p>
      <div class="newsletter__form"><span>ENTER YOUR EMAIL</span><b>SUBMIT</b></div>
    </div>
  </section>
  <section class="widget">
    <h3 class="widget__head widget__head--white">RSS Feed</h3>
    <div class="widget__body" style="height:73px;padding-top:12px">
      <ul class="dot-list dot-list--plain"><li>RSS - Posts</li></ul>
    </div>
  </section>
</aside>

</body>
</html>
```